Attractive door board for entrance beautysalon

Make an attractive design for a board that can be glued on the front door of a beauty salon. The salon location has no window in the front so I need something catchy and attractive. The door board contains a list of the services and the website: www.velmora.be, and the text "Enkel op afspraak, bel 0486319542"

Target Market(s)

woman between 16 and 99 years old

Industry/Entity Type

Beauty Salon

Font styles to use
Sans Serif

Requirements
Must have
• A very nice, attractive but sober design.
• It must have a classy Marvaux, Quen, ... chique design.
• The logo must be on it (in attachment)
• There must be the following list in it:
• Gelaatsverzorging
• Wimperverlenging
• Wimperlifting
• Suikerontharing
• Permanente Make Up
• Airbrush Tanning
• Manicure - Pedicure - Tovira
• and then the website www.velmora.be, and the text "Enkel op afspraak, bel 0486319542"
Nice to have
• a catchy design,
• max. width can be 75 cm and max height 180 cm as it is a design for a board that will be glued on a door.
Should not have
• orchid flowers, buddha look a likes

```html
<!DOCTYPE html>
<html lang="nl">
<head>
<meta charset="utf-8">
<title>Velmora – Deurbord</title>
<link rel="stylesheet" href="https://fonts.googleapis.com/css2?family=Crimson+Pro:wght@400;600&family=Montserrat:wght@400;500&display=swap">
<style>
  :root {
    --ink: #000000;
    --paper: #ffffff;
    --rose: #e3334a;
    --rose-deep: #c81f37;
    --blossom: #f4a7b0;
    --shadow-bloom: #5a4548;
    --service-red: #e8323f;
  }
  * { margin: 0; padding: 0; box-sizing: border-box; }
  html, body { width: 1200px; height: 2877px; overflow: hidden; background: var(--ink); }
  .door-board { position: relative; width: 1200px; height: 2877px; background: var(--ink); overflow: hidden; }
  .backdrop { position: absolute; inset: 0; }
  .brand { position: absolute; left: 120px; top: 290px; color: var(--paper); }
  .brand-name {
    font-family: "Montserrat", sans-serif; font-weight: 400;
    font-size: 64px; letter-spacing: 20px; line-height: 1;
  }
  .brand-tagline {
    margin-top: 26px;
    font-family: "Montserrat", sans-serif; font-weight: 500;
    font-size: 20px; letter-spacing: 9px;
  }
  .services {
    position: absolute; right: 42px; top: 1800px;
    list-style: none; text-align: right;
    font-family: "Crimson Pro", serif; font-size: 58px; line-height: 116px;
    color: var(--service-red);
  }
  .contact {
    position: absolute; right: 42px; top: 2640px; text-align: right;
    font-family: "Crimson Pro", serif; font-weight: 600; color: var(--paper);
    font-size: 44px; line-height: 86px;
  }
</style>
</head>
<body>
<main class="door-board">
  <svg class="backdrop" width="1200" height="2877" viewBox="0 0 1200 2877">
    <defs>
      <linearGradient id="bloom-light" x1="0" y1="0" x2="0.6" y2="1">
        <stop offset="0" stop-color="var(--blossom)" stop-opacity="0.85"/>
        <stop offset="1" stop-color="var(--rose-deep)" stop-opacity="0.3"/>
      </linearGradient>
      <linearGradient id="bloom-dark" x1="1" y1="0" x2="0" y2="1">
        <stop offset="0" stop-color="var(--shadow-bloom)" stop-opacity="0.9"/>
        <stop offset="1" stop-color="var(--ink)" stop-opacity="0"/>
      </linearGradient>
    </defs>
    <polygon class="frame-edge" points="34,534 1050,534 34,2740" fill="var(--paper)"/>
    <line class="frame-stroke" x1="1050" y1="534" x2="1200" y2="80" stroke="var(--paper)" stroke-width="10"/>
    <polygon class="accent-panel" points="34,580 1006,580 34,2645" fill="var(--rose)"/>
    <rect class="tulip-art" x="80" y="700" width="600" height="1400" rx="300"
          fill="url(#bloom-light)" role="img" aria-label="Illustratie van roze tulpen"/>
    <rect class="tulip-art-dark" x="830" y="560" width="370" height="760" rx="180"
          fill="url(#bloom-dark)" role="img" aria-label="Illustratie van donkere tulpen"/>
  </svg>

  <header class="brand">
    <div class="brand-name">VELMORA</div>
    <div class="brand-tagline">SCHOONHEIDSINSTITUUT</div>
  </header>

  <ul class="services">
    <li>Gelaatsverzorging</li>
    <li>- Wimperverlenging</li>
    <li>- Wimperlifting</li>
    <li>- Suikerontharing</li>
    <li>- Permanente Make Up</li>
    <li>- Airbrush Tanning</li>
    <li>- Manicure - Pedicure - Tovira</li>
  </ul>

  <footer class="contact">
    <p class="contact-web">www.velmora.be</p>
    <p class="contact-call">"Enkel op afspraak, bel 0486319542"</p>
  </footer>
</main>
</body>
</html>
```